Design for a 3-4 screens mobile app

The app is a "simple" ordering mobile app.
1. START screen : user can select either "NEW order" either "VIEW history" - or, can access the usual Contact, About, and Conditions pages.
2. NEW order : is a sequence of 3 basic screens/forms made of 3-4 fields each. Logic is the following: you select the service you need, its recurrence, mention where you are located and then you post it towards the marketplace...
3. VIEW history : is where you land at the end of the ordering process - and accessible from START screen. You see there your previous orders, and their statuses.
Mandatory : we need design for START screen, NEW order and VIEW history screens.
Design but be optimized for Smartphones, used in Portrait mode.
Please take into account the design of the website promoting the Mobile App: https://tidyvanlane.be/
Optional but of course nice to have if you could propose some design or guidance for Contact, About, and Conditions pages...
Here attached a full screen sequence.
Updates
Thanks for all your proposals ! They were submitted to the final customer, he selects one ASAP !
Number of Pages Required
3 page
Look and feel
Each slider illustrates characteristics of the customer's brand and the style your logo design should communicate.

```html
<!DOCTYPE html>
<html lang="en">
<head>
<meta charset="utf-8">
<title>Tidy Van Lane – App screens</title>
<link href="https://fonts.googleapis.com/css2?family=Montserrat:wght@300;400;500;600;700&family=Open+Sans:wght@400;600;700&display=swap" rel="stylesheet">
<style>
:root{
  --backdrop:#fdd0b0;
  --orange:#d95300;
  --orange-bright:#ff6303;
  --orange-light:#f99a3a;
  --header:#e37c40;
  --circle:#8a2f05;
  --white:#ffffff;
  --green:#1ea84a;
  --red:#ff2405;
  --ink:#1a1a1a;
}
*{margin:0;padding:0;box-sizing:border-box}
html,body{width:1200px;height:1161px;overflow:hidden}
body{background:var(--backdrop);position:relative;font-family:"Montserrat",sans-serif;color:var(--white)}
.corner-band{position:absolute;inset:0}
.screen{position:absolute;width:251px;height:447px;background:var(--orange);overflow:hidden}
.screen--start{left:166px;top:38px}
.screen--order{left:482px;top:38px;background:radial-gradient(ellipse 260px 200px at 100% 100%,var(--orange-light),rgba(217,83,0,0) 80%),var(--orange)}
.screen--status{left:798px;top:38px;background:radial-gradient(ellipse 200px 300px at 100% 30%,var(--orange-light),rgba(217,83,0,0) 75%),var(--orange)}
.screen--home{left:166px;top:525px}
.status-bar{position:absolute;left:0;top:0;width:100%;height:15px;background:var(--white);color:var(--ink);font-family:"Open Sans",sans-serif;font-size:8px;font-weight:600}
.status-bar .carrier{position:absolute;left:22px;top:2px}
.status-bar .time{position:absolute;left:0;right:0;text-align:center;top:2px}
.status-bar .battery{position:absolute;right:20px;top:5px;width:16px;height:5px;background:var(--ink);border-radius:1px}
.abs{position:absolute}
.center{left:0;right:0;text-align:center}
.brand-mark{background:var(--orange-light)}
.brand-name{font-family:"Open Sans",sans-serif;font-weight:700;font-size:11px;color:var(--orange-light)}
.welcome{font-family:"Open Sans",sans-serif;font-size:6.4px;line-height:10px;color:var(--white)}
.divider-dots{border-top:1px dotted rgba(255,255,255,.6)}
.hex{position:absolute;width:22px;height:22px;left:50%;margin-left:-11px}
.contact-label{font-family:"Open Sans",sans-serif;font-size:7.4px}
.contact-value{font-family:"Open Sans",sans-serif;font-size:12.5px;font-weight:400}
.band-bright{position:absolute;left:0;width:100%;background:var(--orange-bright)}
.app-header{position:absolute;left:0;top:15px;width:100%;height:35px;background:var(--header)}
.back-btn{position:absolute;left:20px;top:20px;width:29px;height:27px;background:var(--white);color:var(--orange);font-size:4.5px;text-align:center;font-weight:600}
.form-row{position:absolute;left:52px;width:168px}
.row-icon{position:absolute;width:25px;height:25px;border-radius:50%;background:var(--circle);left:0}
.row-text{position:absolute;left:30px;font-size:7px;line-height:9px}
.row-text b{font-weight:700}
.row-text .big{font-size:12px;line-height:13px}
.row-rule{position:absolute;left:52px;width:168px;border-top:1px solid rgba(255,255,255,.3)}
.btn{position:absolute;font-size:6.4px;font-weight:700;letter-spacing:.3px;text-align:center;color:var(--white)}
.btn--green{background:var(--green)}
.btn--red{background:var(--red)}
.status-title{font-size:12px;font-weight:400;letter-spacing:.3px}
.order-icon{position:absolute;width:40px;height:40px;border-radius:50%;background:var(--circle);left:22px}
.order-name{position:absolute;left:69px;font-size:8px;font-weight:600}
.order-detail{position:absolute;left:69px;font-size:6px;line-height:13.5px}
.muted{color:rgba(120,40,0,.75)}
.tab-label{font-size:6.4px;color:rgba(255,255,255,.85)}
.caption{position:absolute;font-family:"Montserrat",sans-serif;font-weight:400;color:var(--white)}
.caption-list{left:796px;top:905px;font-size:29px;line-height:45px;letter-spacing:2px}
.caption-size{left:532px;top:1043px;font-size:48px;letter-spacing:3px}
</style>
</head>
<body>

<svg class="corner-band" width="1200" height="1161" viewBox="0 0 1200 1161" aria-hidden="true">
  <polygon points="1200,549 1200,1161 296,1161" fill="#d95300"/>
</svg>

<!-- Start screen -->
<section class="screen screen--start">
  <div class="status-bar"><span class="carrier">Carrier</span><span class="time">2:32 PM</span><span class="battery"></span></div>
  <div class="abs brand-mark" style="left:88px;top:45px;width:75px;height:75px"></div>
  <div class="abs center brand-name" style="top:131px">Tidy Van Lane</div>
  <p class="abs welcome" style="left:47px;width:160px;top:152px">Welcome on Tidy Van Lane, should you have any question about this App or our services, do not hesitate to</p>
  <div class="abs divider-dots" style="left:55px;width:140px;top:196px"></div>
  <svg class="hex" style="top:210px" viewBox="0 0 22 22"><polygon points="11,1 20,6 20,16 11,21 2,16 2,6" fill="none" stroke="#fff" stroke-width=".8"/><path d="M8 8c0 4 2 6 6 6l1-1.5-2-1-1 1c-1-.5-2-1.5-2.5-2.5l1-1-1-2z" fill="none" stroke="#fff" stroke-width=".7"/></svg>
  <div class="abs center contact-label" style="top:234px">Call us on</div>
  <div class="abs center contact-value" style="top:244px">+32 470 12 34 56</div>
  <div class="band-bright" style="top:271px;height:74px"></div>
  <svg class="hex" style="top:282px" viewBox="0 0 22 22"><polygon points="11,1 20,6 20,16 11,21 2,16 2,6" fill="none" stroke="#fff" stroke-width=".8"/><path d="M7 9h8v5H7zM7 9l4 3 4-3" fill="none" stroke="#fff" stroke-width=".7"/></svg>
  <div class="abs center contact-label" style="top:306px">Sends us an email at</div>
  <div class="abs center contact-value" style="top:315px">info@tidyvanlane.be</div>
  <svg class="hex" style="top:356px" viewBox="0 0 22 22"><polygon points="11,1 20,6 20,16 11,21 2,16 2,6" fill="none" stroke="#fff" stroke-width=".8"/><path d="M7 11l8-4-3 8-1.5-3z" fill="none" stroke="#fff" stroke-width=".7"/></svg>
  <div class="abs center contact-label" style="top:383px">Visit our Website at</div>
  <div class="abs center contact-value" style="top:393px">tidyvanlane.be</div>
</section>

<!-- New order screen -->
<section class="screen screen--order">
  <div class="status-bar"><span class="carrier">Carrier</span><span class="time">2:32 PM</span><span class="battery"></span></div>
  <div class="app-header"></div>
  <div class="back-btn"><svg width="14" height="14" viewBox="0 0 14 14" style="margin-top:3px"><circle cx="7" cy="7" r="6" fill="#d95300"/><path d="M9.5 7H5M7 4.8L4.8 7 7 9.2" stroke="#fff" stroke-width="1.3" fill="none"/></svg><div>BACK</div></div>
  <svg class="abs" style="left:126px;top:24px" width="18" height="18" viewBox="0 0 22 22"><polygon points="11,1 20,6 20,16 11,21 2,16 2,6" fill="none" stroke="#fff" stroke-width=".9"/><path d="M11 9v4M9 11h4" stroke="#fff" stroke-width=".8"/></svg>
  <svg class="abs" style="left:306px;top:24px;left:306px" width="0" height="0"></svg>
  <svg class="abs" style="left:146px;top:24px;left:306px" width="0" height="0"></svg>
  <svg class="abs" style="left:146px;top:24px;left:146px;left:146px" width="0" height="0"></svg>
  <svg class="abs" style="left:146px;top:24px;left:146px" width="0" height="0"></svg>
  <svg class="abs" style="left:146px;top:24px" width="0" height="0"></svg>
  <svg class="abs" style="left:146px;top:24px;left:146px" width="0" height="0"></svg>
  <svg class="abs" style="left:146px;top:24px" width="0" height="0"></svg>
  <svg class="abs" style="left:146px;top:24px" width="18" height="18" viewBox="0 0 22 22"><polygon points="11,1 20,6 20,16 11,21 2,16 2,6" fill="none" stroke="#fff" stroke-width=".9"/><rect x="7.5" y="8.5" width="7" height="5" fill="none" stroke="#fff" stroke-width=".8"/></svg>

  <div class="form-row" style="top:73px"><div class="row-icon"></div><div class="row-text" style="top:8px;font-size:8px">I need <b>IRONING</b></div></div>
  <div class="row-rule" style="top:109px"></div>
  <div class="form-row" style="top:117px"><div class="row-icon"></div><div class="row-text" style="top:8px;font-size:8px">For 4 hours</div></div>
  <div class="row-rule" style="top:152px"></div>
  <div class="form-row" style="top:163px"><div class="row-icon"></div><div class="row-text" style="top:3px">Frequency<br>On a weekly basis</div></div>
  <div class="row-rule" style="top:196px"></div>
  <div class="form-row" style="top:207px"><div class="row-icon"></div><div class="row-text" style="top:2px"><b>CALL ME ON</b><br><span class="big">0470112233</span></div></div>
  <div class="row-rule" style="top:239px"></div>
  <div class="form-row" style="top:249px"><div class="row-icon"></div><div class="row-text" style="top:2px"><b>Vouchly client number</b><br><span class="big">987654321000</span></div></div>
  <div class="row-rule" style="top:282px"></div>
  <div class="form-row" style="top:294px"><div class="row-icon"></div><div class="row-text" style="top:3px"><b>VAUCHER FORMAT</b><br>Papier</div></div>
  <div class="row-rule" style="top:326px"></div>
  <div class="form-row" style="top:337px"><div class="row-icon"></div><div class="row-text" style="top:3px;white-space:nowrap"><b>AT THIS ADDRESS</b><br>Rue des Tilleuls 8, 1050 Ixelles</div></div>
  <div class="btn btn--green" style="left:52px;top:382px;width:147px;height:21px;line-height:21px">SEND REQUEST</div>
</section>

<!-- Request status screen -->
<section class="screen screen--status">
  <div class="status-bar"><span class="carrier">Carrier</span><span class="time">2:32 PM</span><span class="battery"></span></div>
  <div class="app-header" style="background:linear-gradient(90deg,var(--header),#f29a55)"></div>
  <div class="abs center status-title" style="top:25px">REQUEST STATUS</div>
  <div class="order-icon" style="top:65px"></div>
  <div class="order-name" style="top:80px">Windows cleaning</div>
  <div class="order-detail muted" style="top:105px">3 hours-twice a month<br>Rue des Tilleuls 8, 1050 BXL<br>Date: to be implemented...</div>
  <svg class="abs" style="left:173px;top:149px" width="14" height="14" viewBox="0 0 14 14"><circle cx="7" cy="7" r="6.3" fill="none" stroke="#fff" stroke-width=".7"/><path d="M4.5 7h5" stroke="#fff" stroke-width=".7"/></svg>
  <div class="abs" style="left:190px;top:152px;font-size:5.5px">pending</div>
  <div class="abs" style="left:56px;top:174px;width:162px;border-top:1px solid rgba(255,255,255,.3)"></div>
  <div class="order-icon" style="top:194px"></div>
  <div class="order-name" style="top:209px">IRONING</div>
  <div class="order-detail" style="top:234px">4hours- on a weekly basis<br>Chemin des Prés 4, 5000 Namur<br>Date: to be implemented...<br>Request accepted by agency</div>
  <div class="btn btn--green" style="left:53px;top:308px;width:146px;height:22px;line-height:22px">ACCEPT</div>
  <div class="btn btn--red" style="left:53px;top:343px;width:146px;height:23px;line-height:23px">REFUSE</div>
</section>

<!-- Home screen with tabs -->
<section class="screen screen--home">
  <div class="status-bar"><span class="carrier">Carrier</span><span class="time">2:32 PM</span><span class="battery"></span></div>
  <div class="app-header" style="top:14px;height:43px"></div>
  <svg class="abs" style="left:77px;top:22px" width="18" height="18" viewBox="0 0 22 22"><polygon points="11,1 20,6 20,16 11,21 2,16 2,6" fill="none" stroke="#fff" stroke-width=".9"/><path d="M11 9v4M9 11h4" stroke="#fff" stroke-width=".8"/></svg>
  <div class="abs tab-label" style="left:70px;top:43px">New Order</div>
  <svg class="abs" style="left:157px;top:22px" width="18" height="18" viewBox="0 0 22 22"><polygon points="11,1 20,6 20,16 11,21 2,16 2,6" fill="none" stroke="#fff" stroke-width=".9"/><rect x="7.5" y="8.5" width="7" height="5" fill="none" stroke="#fff" stroke-width=".8"/></svg>
  <div class="abs tab-label" style="left:148px;top:43px">View screen</div>
  <div class="abs brand-mark" style="left:95px;top:76px;width:59px;height:58px"></div>
  <div class="abs center brand-name" style="top:146px">Tidy Van Lane</div>
  <p class="abs welcome" style="left:43px;width:170px;top:167px">Welcome on Tidy Van Lane, should you have any question about this App or our services, do not hesitate to</p>
  <div class="abs divider-dots" style="left:55px;width:140px;top:198px"></div>
  <svg class="hex" style="top:211px" viewBox="0 0 22 22"><polygon points="11,1 20,6 20,16 11,21 2,16 2,6" fill="none" stroke="#fff" stroke-width=".8"/><path d="M8 8c0 4 2 6 6 6l1-1.5-2-1-1 1c-1-.5-2-1.5-2.5-2.5l1-1-1-2z" fill="none" stroke="#fff" stroke-width=".7"/></svg>
  <div class="abs center contact-label" style="top:236px">Call us on</div>
  <div class="abs center contact-value" style="top:246px">+32 470 12 34 56</div>
  <div class="band-bright" style="top:283px;height:74px"></div>
  <svg class="hex" style="top:294px" viewBox="0 0 22 22"><polygon points="11,1 20,6 20,16 11,21 2,16 2,6" fill="none" stroke="#fff" stroke-width=".8"/><path d="M7 9h8v5H7zM7 9l4 3 4-3" fill="none" stroke="#fff" stroke-width=".7"/></svg>
  <div class="abs center contact-label" style="top:318px">Sends us an email at</div>
  <div class="abs center contact-value" style="top:327px">info@tidyvanlane.be</div>
  <svg class="hex" style="top:371px" viewBox="0 0 22 22"><polygon points="11,1 20,6 20,16 11,21 2,16 2,6" fill="none" stroke="#fff" stroke-width=".8"/><path d="M7 11l8-4-3 8-1.5-3z" fill="none" stroke="#fff" stroke-width=".7"/></svg>
  <div class="abs center contact-label" style="top:398px">Visit our Website at</div>
  <div class="abs center contact-value" style="top:408px">tidyvanlane.be</div>
</section>

<div class="caption caption-list">1.Start screen<br>2.Now order<br>3. View history</div>
<div class="caption caption-size">720x1280px presentation</div>

</body>
</html>
```